Sign Up Page Design

We wish to revamp the sign up page of our real estate website (www.trellisparcelmarket.com) in order to improve conversion rate. This sign up page has two steps, thus you should come up with 2 pages of sample. We are more interested in getting a design created by a UX designer who has already created other sign up pages and knows the mind of an online buyer. We are sending attached the screenshot of the current sign up page for you to take as basis. Feel free to improve them and come up with something better which can help increase conversion rate.
Updates

We have changed the project settings to NON REFUNDABLE.... so please keep sending your designs. We look forward for your creativity!!!

Industry/Entity Type

Real Estate

```html
<!DOCTYPE html>
<html lang="en">
<head>
<meta charset="utf-8">
<title>Trellis Parcel Market – Choose Your Plan</title>
<link href="https://fonts.googleapis.com/css2?family=Open+Sans:wght@400;600;700;800&display=swap" rel="stylesheet">
<style>
:root{
  --bg-grey:#e6e6e6;
  --header-grey:#d9d9d9;
  --text-grey:#5f5f5f;
  --orange:#f7931e;
  --orange-dark:#f56e07;
  --yellow:#ffc400;
  --blue:#1f7dc3;
  --blue-dark:#11588f;
  --blue-title:#1a6aa8;
  --green:#6aa536;
  --green-dark:#4f8a26;
  --taupe:#c9c2bf;
  --footer:#4d4d4d;
  --white:#ffffff;
}
*{box-sizing:border-box;margin:0;padding:0}
html,body{width:1174px;height:1200px;overflow:hidden}
body{position:relative;font-family:"Open Sans",Arial,sans-serif;background:var(--white);color:var(--text-grey)}
.abs{position:absolute}
.stage{left:0;top:0;width:1174px;height:743px;background:linear-gradient(#e2e2e2,#ebebeb)}
.header{left:0;top:0;width:1174px;height:73px;background:linear-gradient(#dcdcdc,#cfcfcf);border-bottom:3px solid #f0f0f0}
.brand{left:0;width:1174px;top:24px;display:flex;justify-content:center;align-items:center;gap:10px;font-weight:700;font-size:22px;color:var(--blue-title)}
.brand-mark{width:26px;height:26px;border-radius:50%;background:var(--orange)}
.headline{left:0;width:1174px;top:104px;text-align:center;font-size:35px;letter-spacing:1px;color:var(--text-grey)}
.headline .o{color:var(--orange);font-weight:600}.headline .b{color:var(--blue-title);font-weight:600}.headline .g{color:var(--green);font-weight:600}
.plan{width:241px;height:256px;border-radius:14px;background:linear-gradient(var(--blue) 0,var(--blue) 56%,var(--blue-dark) 100%);color:var(--white);overflow:hidden;box-shadow:0 2px 4px rgba(0,0,0,.15)}
.plan .top{height:141px;text-align:center;background:linear-gradient(#3096da,#1c76bb)}
.plan .name{padding-top:38px;font-weight:800;font-size:25px;letter-spacing:.5px}
.plan .price{font-weight:800;font-size:38px;line-height:1.15}
.plan .perks{padding:12px 0 0 18px;font-size:12.5px;line-height:1.55}
.perk{display:flex;gap:8px;align-items:flex-start}
.rule{left:4px;right:4px;border-top:1px solid rgba(255,255,255,.45)}
.choice{left:0;right:0;text-align:center;font-weight:700;font-size:15px;display:flex;justify-content:center;align-items:center;gap:10px}
.radio{width:11px;height:11px;border-radius:50%;background:#d8d8d8;border:1px solid #aaa;display:inline-block}
.radio.on{background:var(--white);box-shadow:inset 0 0 0 3px var(--blue)}
.trial{left:468px;top:181px;width:264px;height:359px;border-radius:16px;background:linear-gradient(var(--yellow),var(--orange) 45%,var(--orange-dark));color:var(--white);text-align:center}
.ribbon{left:458px;top:198px;width:284px;height:37px;background:linear-gradient(#86be45,var(--green));color:var(--white);font-size:18px;text-align:center;line-height:37px}
.trial .name{padding-top:72px;font-weight:800;font-size:36px;color:#5a3b12}
.trial .deal{padding-top:43px;font-weight:800;font-size:20px;line-height:1.3}
.pay-label{left:447px;top:594px;font-size:20px;font-weight:600;color:var(--blue-title);letter-spacing:.5px}
.btn{top:652px;height:43px;border-radius:6px;display:flex;align-items:center;justify-content:center;gap:10px}
.btn-back{left:268px;width:108px;background:linear-gradient(#2f86cf,#0f5b9c);color:var(--white);font-weight:700;font-size:20px;border:2px solid #9cc6e8}
.btn-pay{background:linear-gradient(#fff,#efefef);box-shadow:0 1px 3px rgba(0,0,0,.2);font-size:16px;color:#444}
.btn-go{left:757px;width:259px;background:linear-gradient(#f7941e,#e06a00);color:var(--white);font-weight:700;font-size:20px;border:2px solid #f9c186}
.circle-ico{width:18px;height:18px;border-radius:50%;background:var(--white);display:flex;align-items:center;justify-content:center}
.pay-icon{width:38px;height:30px;border-radius:3px}
.quote{top:759px;width:461px;height:157px;font-size:11.5px;letter-spacing:.6px;line-height:14px;text-align:center}
.quote .photo{left:24px;top:10px;width:134px;height:140px;border-radius:50%;background:radial-gradient(circle at 50% 45%,#d9a87d,#8a5b34)}
.quote .text{left:174px;top:34px;width:280px}
.quote .by{left:178px;top:122px;font-size:13.5px;letter-spacing:0}
.tail{width:0;height:0}
.q-grey{left:120px;background:var(--taupe);color:#333}
.q-green{left:606px;background:var(--green);color:var(--white)}
.qmark{font-size:50px;font-weight:800;line-height:1;opacity:.6}
.divider{left:90px;width:994px;top:948px;height:2px;background:linear-gradient(90deg,transparent,#ddd 20%,#ddd 80%,transparent)}
.badge{background:#d8d8d8;border-radius:6px}
.secure{left:722px;top:991px;font-size:12.5px;color:#333;line-height:1.6}
.note{left:337px;top:1062px;width:600px;font-size:10.5px;line-height:18px;color:#555}
.footer{left:0;top:1149px;width:1174px;height:51px;background:var(--footer);color:#c9c9c9;font-size:12.5px;text-align:center;padding-top:10px;line-height:18px}
</style>
</head>
<body>
<div class="abs stage"></div>
<header class="abs header"></header>
<div class="abs brand"><span class="brand-mark"></span>Trellis Parcel Market</div>

<h1 class="abs headline" style="font-weight:400">CHOOSE THE PLAN <span class="o">THAT'S</span> <span class="b">RIGHT</span> <span class="g">FOR YOU</span></h1>

<section class="abs plan" style="left:200px;top:206px">
  <div class="top"><div class="name">Monthly</div><div class="price">$39.95/mo</div></div>
  <div class="perks" style="padding-top:12px">
    <div class="perk"><svg width="22" height="22" viewBox="0 0 22 22"><rect x="1" y="5" width="15" height="15" fill="none" stroke="#8cc63f" stroke-width="2"/><path d="M4 12l4 4 11-13" fill="none" stroke="#8cc63f" stroke-width="3"/></svg><span>Cancle at any time during<br>your monthly subscription</span></div>
  </div>
  <div class="abs rule" style="top:214px"></div>
  <div class="abs choice" style="top:226px"><span class="radio"></span>I'll go monthly</div>
</section>

<section class="abs trial">
  <div class="name">7-Day Trail*</div>
  <div class="deal">WAS $9.95 NOW<br>$3.95<br>ACT NOW!</div>
  <div class="abs rule" style="left:8px;right:8px;top:310px"></div>
  <div class="abs choice" style="top:324px"><span class="radio on"></span>I'll try for 7 days</div>
</section>
<div class="abs ribbon">Limited time offer</div>

<section class="abs plan" style="left:769px;top:206px">
  <div class="top"><div class="name">Annual</div><div class="price">$99.00/mo</div></div>
  <div class="perks" style="padding:10px 0 0 20px;font-size:13px;line-height:25px">
    <div class="perk" style="align-items:center"><svg width="12" height="12" viewBox="0 0 12 12"><rect x="1" y="2" width="9" height="9" fill="none" stroke="#8cc63f"/><path d="M3 6l2 3 6-8" fill="none" stroke="#8cc63f" stroke-width="2"/></svg>Only $8.25/mo gfor 12 months!</div>
    <div class="perk" style="align-items:center"><svg width="12" height="12" viewBox="0 0 12 12"><rect x="1" y="2" width="9" height="9" fill="none" stroke="#8cc63f"/><path d="M3 6l2 3 6-8" fill="none" stroke="#8cc63f" stroke-width="2"/></svg>One times fee only-No Rebill</div>
  </div>
  <div class="abs rule" style="top:214px"></div>
  <div class="abs choice" style="top:228px"><span class="radio"></span>I'll go Annual</div>
</section>

<svg class="abs" style="left:418px;top:606px" width="30" height="34" viewBox="0 0 30 34"><path d="M26 2C12 2 6 10 8 22l-6-2 10 12 6-14-6 3C11 12 16 6 26 2z" fill="#f7931e"/></svg>
<div class="abs pay-label">Chose Your Payment From:-</div>

<div class="abs btn btn-back"><span class="circle-ico"><svg width="10" height="10" viewBox="0 0 10 10"><path d="M7 1L2 5l5 4z" fill="#11588f"/></svg></span>Back</div>
<div class="abs btn btn-pay" style="left:393px;width:166px"><span class="radio on"></span>Credit Card<span class="pay-icon" role="img" aria-label="Credit card icon" style="background:linear-gradient(135deg,#f7c23a,#2b8ad1)"></span></div>
<div class="abs btn btn-pay" style="left:575px;width:166px"><span class="radio"></span>Cheque<span class="pay-icon" role="img" aria-label="Cheque icon" style="width:46px;background:linear-gradient(135deg,#fbe3e3,#e04848)"></span></div>
<div class="abs btn btn-go">Proceed To Checkout<span class="circle-ico"><svg width="10" height="10" viewBox="0 0 10 10"><path d="M3 1l5 4-5 4z" fill="#e06a00"/></svg></span></div>

<article class="abs quote q-grey">
  <div class="abs photo" role="img" aria-label="Portrait photo of a smiling customer"></div>
  <div class="abs qmark" style="left:150px;top:4px;color:#888">“</div>
  <p class="abs text">Lorem Ipsum has been the industry's standard dummy text ever since the 1500s, when an unknown printer took a galley of type and scram The Service here is great. I would highly recommend it solutions to anybody wanting</p>
  <p class="abs by">- John Doe, Brightway Homes</p>
</article>
<svg class="abs" style="left:512px;top:915px" width="24" height="25" viewBox="0 0 24 25"><path d="M0 0h24L0 25z" fill="#c9c2bf"/></svg>

<article class="abs quote q-green">
  <div class="abs photo" role="img" aria-label="Portrait photo of a smiling customer"></div>
  <div class="abs qmark" style="left:150px;top:4px;color:#bfe09c">“</div>
  <p class="abs text" style="top:42px">Lorem Ipsum has been the industry's standard dummy text ever since the 1500s, when an unknown printer took a galley of type and scram The Service here is great. I would highly recommend it solutions to anybody wanting</p>
  <p class="abs by" style="top:133px">- John Doe, Brightway Homes</p>
</article>
<svg class="abs" style="left:988px;top:916px" width="24" height="25" viewBox="0 0 24 25"><path d="M0 0h24L0 25z" fill="#6aa536"/></svg>

<div class="abs divider"></div>

<div class="abs badge" style="left:403px;top:980px;width:125px;height:56px" role="img" aria-label="Security certificate badge"></div>
<div class="abs badge" style="left:570px;top:982px;width:92px;height:54px" role="img" aria-label="Payment processor badge"></div>
<svg class="abs" style="left:692px;top:992px" width="22" height="32" viewBox="0 0 22 32"><path d="M5 14V9a6 6 0 0 1 12 0v5" fill="none" stroke="#666" stroke-width="3"/><rect x="1" y="13" width="20" height="18" rx="5" fill="#3b6ea8"/><circle cx="11" cy="22" r="3" fill="#fff"/></svg>
<div class="abs secure">Secure Page<br>128-bit Strong Encryption</div>

<p class="abs note">* If you would like to continue receiving our services beyond the 7-day trial period, simply do nothing and you will only be charged $39.95 per month. There is a "Contact" button on top of every page throughout the entire site that will redirect you to an area where you can end your membership - no questions asked.</p>

<footer class="abs footer">TrellisParcelMarket.com, 420 Alder Crest Way, 12, Harbor Point, FL 33010 &nbsp;&nbsp;&nbsp;|&nbsp;&nbsp;&nbsp; FAX: 1-555-014-2290<br>Terms and ConditionsPrivacy PolicyCopyright © 1998-2014 TrellisParcelMarket.com Inc., All Rights Reserved.</footer>
</body>
</html>
```